23rd Annual Harrowgate Lantern Film Festival Poster

Design an eye catchy, stylish poster for our 23rd film festival. Be different not just a poster with a film reel. Think outside of the box with a design that will attract peoples attention. Colorful (you choose the colors). Make it fun and creative, like the film festival. Show your talents in the design. Be sure it is new and stylish. Dates are August 21 - 29, 2020. Poster size will be 27 inches by 40 inches

Target Market(s)

Upper Middle class - movie lovers

Font styles to use
Sans Serif

Colors
33a6d7

Requirements
Must have
• NO CLIP ART - be original !
Nice to have
• abstract - think outside the box
Should not have
• CLIP ART

```html
<!DOCTYPE html>
<html lang="en">
<head>
<meta charset="utf-8">
<title>23rd Annual Harrowgate Lantern Film Festival — Poster Series</title>
<link href="https://fonts.googleapis.com/css2?family=Archivo+Black&family=Inter:wght@600&display=swap" rel="stylesheet">
<style>
  :root {
    --page-bg: #efe9e4;

    --violet-bg: #6f5bbf;
    --violet-ink: #d9d33c;
    --violet-art-a: #7b4fd0;
    --violet-art-b: #3aa37a;
    --violet-art-c: #33a6d7;

    --teal-bg: #5b9cb2;
    --teal-ink: #ff2c7c;
    --teal-art-a: #c9c24a;
    --teal-art-b: #2bd61f;
    --teal-art-c: #6aa2c0;

    --coral-bg: #d9564f;
    --coral-ink: #2ff07e;
    --coral-art-a: #4f63d8;
    --coral-art-b: #8a1ed8;
    --coral-art-c: #d0605a;
  }

  * { margin: 0; padding: 0; box-sizing: border-box; }

  html, body {
    width: 1200px;
    height: 800px;
    overflow: hidden;
    background: var(--page-bg);
  }

  .poster-series {
    position: relative;
    width: 1200px;
    height: 800px;
    display: flex;
    justify-content: center;
    align-items: center;
    gap: 40px;
  }

  .poster {
    position: relative;
    width: 320px;
    height: 474px;
    background: var(--poster-bg);
    overflow: hidden;
  }

  .poster--violet { --poster-bg: var(--violet-bg); --ink: var(--violet-ink); --art-a: var(--violet-art-a); --art-b: var(--violet-art-b); --art-c: var(--violet-art-c); }
  .poster--teal   { --poster-bg: var(--teal-bg);   --ink: var(--teal-ink);   --art-a: var(--teal-art-a);   --art-b: var(--teal-art-b);   --art-c: var(--teal-art-c); }
  .poster--coral  { --poster-bg: var(--coral-bg);  --ink: var(--coral-ink);  --art-a: var(--coral-art-a);  --art-b: var(--coral-art-b);  --art-c: var(--coral-art-c); }

  .poster__artwork {
    position: absolute;
    left: 8px;
    top: 6px;
    width: 304px;
    height: 410px;
    background:
      radial-gradient(ellipse 45% 30% at 12% 72%, var(--art-b) 0%, transparent 70%),
      linear-gradient(160deg, var(--art-a) 0%, var(--art-c) 45%, var(--art-a) 100%);
  }

  .poster__headline {
    position: absolute;
    left: 20px;
    top: 16px;
    font-family: "Archivo Black", sans-serif;
    font-size: 28px;
    line-height: 44px;
    letter-spacing: 0.5px;
    text-transform: uppercase;
    color: var(--ink);
  }

  .poster__details {
    position: absolute;
    left: 9px;
    bottom: 17px;
    font-family: "Inter", sans-serif;
    font-weight: 600;
    font-size: 12.5px;
    line-height: 16px;
    text-transform: uppercase;
    color: var(--ink);
  }
</style>
</head>
<body>
  <main class="poster-series">

    <article class="poster poster--violet">
      <div class="poster__artwork" role="img" aria-label="Abstract wavy striped ribbon pattern in violet, green and blue"></div>
      <h1 class="poster__headline">23rd<br>Annual<br>Harrowgate<br>Lantern<br>Film<br>Festival</h1>
      <p class="poster__details">August 21 - 29<br>Tickets: www.hlff-fest.org</p>
    </article>

    <article class="poster poster--teal">
      <div class="poster__artwork" role="img" aria-label="Abstract wavy striped ribbon pattern in yellow, green and teal"></div>
      <h1 class="poster__headline">23rd<br>Annual<br>Harrowgate<br>Lantern<br>Film<br>Festival</h1>
      <p class="poster__details">August 21 - 29<br>Tickets: www.hlff-fest.org</p>
    </article>

    <article class="poster poster--coral">
      <div class="poster__artwork" role="img" aria-label="Abstract wavy striped ribbon pattern in blue, purple and coral"></div>
      <h1 class="poster__headline">23rd<br>Annual<br>Harrowgate<br>Lantern<br>Film<br>Festival</h1>
      <p class="poster__details">August 21 - 29<br>Tickets: www.hlff-fest.org</p>
    </article>

  </main>
</body>
</html>
```